Furniture & Lighting Wholesaler Needs a Product Catalogue/Look Book

Our company, Virelo Supply Co, imports quality hand-made furniture, lighting and decor from South Africa. Our products are well-designed and are designed to be used in up-market hotels and homes. Our primary customers are small- to medium-size retail shops.
We require a +/- 14-16 page look book (concept as per attached image) that will be used both in hard-copy and online. We have all of the necessary high-res images, descriptions/text etc. We need you to propose several design concepts from which we can choose, and then execute the design.
Please visit our website www.virelosupply.example to see the products and their descriptions, as well as to get a feel for our style. Thank you for looking at our project!
Target Market(s)
Boutique Furniture Stores; Interior Designers
Industry/Entity Type
It Company
Font styles to use
Other font styles liked:
- Bauer Bodini and Open Sans Condensed
Look and feel
Each slider illustrates characteristics of the customer's brand and the style your logo design should communicate.

```html
<!DOCTYPE html>
<html lang="en">
<head>
<meta charset="utf-8">
<title>Virelo Supply Co – Look Book Spread</title>
<link rel="stylesheet" href="https://fonts.googleapis.com/css2?family=Josefin+Sans:wght@300;400&family=Open+Sans:wght@400;600&family=Open+Sans+Condensed:wght@300&display=swap">
<style>
  :root {
    --backdrop: #d9d9d9;
    --paper: #ffffff;
    --gold: #aa9c68;
    --gold-text: #b8aa72;
    --ink: #3a3a3a;
    --charcoal: #3d3d3d;
    --charcoal-light: #5c5c5c;
    --label-dark: #2f2f2f;
  }
  * { box-sizing: border-box; margin: 0; padding: 0; }
  html, body { width: 1200px; height: 800px; overflow: hidden; }
  body { background: var(--backdrop); font-family: "Open Sans", sans-serif; position: relative; }

  .spread {
    position: absolute; left: 20px; top: 195px;
    width: 1160px; height: 410px;
    display: flex;
    box-shadow: 0 12px 30px rgba(0,0,0,.18);
  }
  .page { position: relative; width: 580px; height: 410px; overflow: hidden; }

  /* Left page */
  .page--about { background: var(--paper); }
  .page-title {
    position: absolute; left: 58px; top: 62px;
    font-family: "Josefin Sans", sans-serif; font-weight: 300;
    font-size: 36px; letter-spacing: 1px; color: var(--gold);
  }
  .edge-band {
    position: absolute; left: 0; top: 255px; width: 34px; height: 155px;
    background: var(--gold); border-top-right-radius: 24px;
  }
  .page-number {
    position: absolute; left: 0; bottom: 0; width: 30px; height: 30px;
    background: var(--charcoal); border-top-right-radius: 14px;
    color: #ddd; font-size: 9px; display: flex; align-items: center; justify-content: center;
  }
  .feature-card {
    position: absolute; left: 78px; top: 118px; width: 262px; height: 262px;
    border-radius: 18px; overflow: hidden; background: var(--gold);
  }
  .feature-photo {
    height: 150px;
    background: linear-gradient(180deg, #5d7286 0%, #9fb0bd 38%, #cfc7b4 62%, #b9a98a 100%);
  }
  .feature-icons {
    display: flex; justify-content: space-around; align-items: flex-start;
    padding: 24px 8px 0;
  }
  .feature {
    width: 60px; text-align: center; color: #fff;
    font-family: "Josefin Sans", sans-serif; font-size: 8.5px; line-height: 1.2;
  }
  .feature svg { display: block; margin: 0 auto 6px; width: 26px; height: 26px; }

  .about-copy {
    position: absolute; left: 358px; top: 58px; width: 200px;
    font-size: 7.4px; line-height: 1.42; color: var(--ink); text-align: justify;
  }
  .about-copy p { margin-bottom: 9px; }
  .about-copy .commitment { color: var(--gold-text); font-weight: 600; text-transform: uppercase; text-align: left; }
  .checklist { list-style: none; }
  .checklist li { position: relative; padding-left: 13px; margin-bottom: 8px; text-align: left; }
  .checklist li::before {
    content: ""; position: absolute; left: 0; top: 2px; width: 7px; height: 7px;
    border: 1px solid var(--ink);
  }
  .checklist li::after {
    content: ""; position: absolute; left: 2px; top: 2px; width: 3px; height: 5px;
    border-right: 1.2px solid var(--ink); border-bottom: 1.2px solid var(--ink); transform: rotate(40deg);
  }
  .web-footer {
    position: absolute; right: 0; bottom: 24px; height: 18px; padding: 0 14px 0 10px;
    background: #ededed; border-top-left-radius: 9px; border-bottom-left-radius: 9px;
    display: flex; align-items: center; gap: 6px; font-size: 6.5px; color: #666;
  }
  .web-footer .mark { width: 8px; height: 8px; border: 1.5px solid var(--charcoal); }

  /* Right page */
  .page--contents {
    background: linear-gradient(115deg, var(--charcoal) 0%, var(--charcoal-light) 45%, #4a4a4a 70%, var(--charcoal) 100%);
  }
  .contents-box {
    position: absolute; left: 180px; top: 110px; width: 300px; height: 192px;
    background: #f4f4f4; border: 3px solid var(--gold); border-radius: 20px;
  }
  .contents-label {
    position: absolute; left: 158px; top: 96px; height: 24px; padding: 0 22px 0 10px;
    background: var(--label-dark); display: flex; align-items: center;
    font-family: "Josefin Sans", sans-serif; font-size: 12px; color: var(--gold-text);
    letter-spacing: .5px;
  }
  .contents-list {
    position: absolute; left: 218px; top: 132px;
    font-family: "Open Sans", sans-serif; font-weight: 600; font-size: 9px;
    line-height: 1.55; color: var(--ink); list-style: none; counter-reset: item;
  }
  .contents-list li { counter-increment: item; display: flex; }
  .contents-list li::before { content: counter(item) "."; width: 26px; font-weight: 400; }
</style>
</head>
<body>
  <div class="spread">
    <section class="page page--about">
      <h1 class="page-title">ABOUT US</h1>
      <div class="edge-band"></div>
      <div class="page-number">2</div>

      <div class="feature-card">
        <div class="feature-photo" role="img" aria-label="Photograph of a herd of elephants crossing a dry savannah under a cloudy sky"></div>
        <div class="feature-icons">
          <div class="feature">
            <svg viewBox="0 0 26 26" fill="none" stroke="#fff" stroke-width="1.3"><rect x="6" y="4" width="14" height="18" rx="1"/><line x1="9" y1="9" x2="17" y2="9"/><line x1="9" y1="13" x2="17" y2="13"/><line x1="9" y1="17" x2="15" y2="17"/></svg>
            Catalogue
          </div>
          <div class="feature">
            <svg viewBox="0 0 26 26" fill="none" stroke="#fff" stroke-width="1.3"><path d="M3 19 Q8 16 13 19 L20 17 Q23 16 22 19 L15 23 L5 23"/><path d="M13 17 V8"/><path d="M13 11 Q8 10 8 5 Q13 6 13 11"/><path d="M13 9 Q18 8 18 3 Q13 4 13 9"/></svg>
            Handmade Craftmanship
          </div>
          <div class="feature">
            <svg viewBox="0 0 26 26" fill="none" stroke="#fff" stroke-width="1.3"><path d="M13 24 C7 16 5 13 5 10 A8 8 0 0 1 21 10 C21 13 19 16 13 24 Z"/><circle cx="13" cy="10" r="3.5"/></svg>
            Manufactured in South Africa
          </div>
          <div class="feature">
            <svg viewBox="0 0 26 26" fill="none" stroke="#fff" stroke-width="1.3"><path d="M5 21 C5 10 12 5 22 5 C22 15 16 21 5 21 Z"/><path d="M5 21 L15 11"/></svg>
            Sustainable
          </div>
        </div>
      </div>

      <div class="about-copy">
        <p>Our style is contemporary "safari chic" while studiously avoiding any overt tribal / African / village handicraft references. Virelo Supply Co offers a wide variety of up-market products for the home such as decorative lighting, furniture, accessories, cushions and rugs. Products are handmade in South Africa, of exotic indigenous materials such as feathers, ostrich eggs, leather, porcupine quills, suede, horns, ostrich skins and a variety of game skins.</p>
        <p class="commitment">We operate a sustainable model of sourcing &amp; manufacturing: all of our products have been sourced from suppliers who are commited to ethical business practices. For clarity this means that:</p>
        <ul class="checklist">
          <li>All animal skulls have been sourced from game reserves where the animal has died in the wild, or been killed during a legislated cull</li>
          <li>All cow horns and leather have been sourced from farms whose primary business is raising cattle as a food source, and who sell the cow horns &amp; skins as a by-product of food production</li>
          <li>The artisans working in the tanneries and factories in which our products are made are paid a living wage, and who work in an environment that is regularly examined by independent regulators.</li>
        </ul>
      </div>

      <div class="web-footer"><span class="mark"></span>www.virelosupply.example</div>
    </section>

    <section class="page page--contents">
      <div class="contents-box"></div>
      <div class="contents-label">TABLE OF CONTENT</div>
      <ol class="contents-list">
        <li>Chandeliers</li>
        <li>Lamps</li>
        <li>Furniture</li>
        <li>Wall Art</li>
        <li>Hides &amp; Skins</li>
        <li>Horns &amp; Skulls</li>
        <li>Decor</li>
        <li>Lamp Shades</li>
        <li>Contact Us</li>
      </ol>
    </section>
  </div>
</body>
</html>
```